update of B2B website and conversion to single page

The current website needs to be modernized. I want what is commonly called a single page website. It is not actually a single page. See some examples here:
https://www.brivane.example/
https://www.quorel.example/
https://www.tindlewick.example/
Most or all graphics will be replaced.
Please see the attached spreadsheet for a rough draft of the home page layout. Convert the existing website at https://www.zolvinbyte.example/ to a single page website. We will provide the page content. You will provide all of the design, graphics, development, production deployment. etc. The look and feel should be corporate, polished, premium.

```html
<!DOCTYPE html>
<html lang="en">
<head>
<meta charset="utf-8">
<title>Zolvinbyte – Enterprise Data Quality Made Easy</title>
<link rel="stylesheet" href="https://fonts.googleapis.com/css2?family=Poppins:wght@400;500;600;700&display=swap">
<style>
:root{
  --navy:#1f2a6b;
  --navy-deep:#17205a;
  --yellow:#fcc736;
  --yellow-soft:#fdd04f;
  --ink:#2a2d3a;
  --muted:#555a66;
  --white:#ffffff;
  --footer-bg:#f3f4f6;
}
*{box-sizing:border-box;margin:0;padding:0}
html,body{width:1200px;height:2719px;overflow:hidden}
body{font-family:"Poppins",Arial,sans-serif;color:var(--ink);background:var(--white);position:relative}
.abs{position:absolute}

/* HERO */
.hero{position:absolute;left:0;top:0;width:1200px;height:716px;overflow:hidden}
.hero-media{position:absolute;inset:0;background:
  radial-gradient(circle at 78% 30%,rgba(120,170,230,.55),transparent 40%),
  radial-gradient(circle at 20% 35%,rgba(110,160,220,.45),transparent 35%),
  linear-gradient(180deg,#2c4a7e 0%,#3a5a88 45%,#4a6690 70%,#2a3f68 100%)}
.topbar{position:absolute;top:12px;left:0;width:1200px;height:26px;color:#fff;font-size:15px}
.topbar .item{position:absolute;top:0;display:flex;align-items:center;gap:7px}
.nav-logo{position:absolute;left:100px;top:62px;display:flex;align-items:center;gap:12px;color:#fff}
.nav-logo .mark{width:34px;height:34px;border-radius:50%;background:#fff}
.nav-logo .name{font-size:34px;font-weight:600;line-height:1}
.nav-logo .tag{position:absolute;left:100px;top:44px;font-size:12px;white-space:nowrap;color:#fff;display:none}
.nav{position:absolute;top:76px;left:430px;display:flex;gap:0;color:#fff;font-size:17px}
.nav a{color:#fff;text-decoration:none;position:absolute;white-space:nowrap}
.follow{position:absolute;left:40px;top:210px;width:24px;color:#fff}
.follow .dot{width:16px;height:16px;border-radius:50%;background:#fff;margin:0 auto 29px}
.follow .line{width:1px;height:60px;background:#fff;margin:0 auto}
.follow .label{position:absolute;left:-26px;top:280px;transform:rotate(-90deg);font-size:15px;white-space:nowrap}
.hero-title{position:absolute;top:312px;left:0;width:1200px;text-align:center;color:#fff;font-size:58px;font-weight:700;letter-spacing:1px}
.hero-sub{position:absolute;top:382px;left:0;width:1200px;text-align:center;color:#fff;font-size:24px;font-weight:500;line-height:37px}
.btn-navy{position:absolute;background:var(--navy);color:#fff;font-weight:600;display:flex;align-items:center;justify-content:center;text-transform:uppercase}
.hero-btn{left:529px;top:467px;width:142px;height:44px;border-radius:22px;font-size:16px}
.slider-dots{position:absolute;left:1146px;top:366px;width:18px}
.slider-dots span{display:block;width:10px;height:10px;border-radius:50%;background:#fff;margin:0 auto}
.slider-dots .active{width:20px;height:20px;border:3px solid #fff;background:transparent;position:relative;margin:20px auto}
.slider-dots .active::after{content:"";position:absolute;inset:3px;border-radius:50%;background:#fff}

/* FEATURES */
.feature{position:absolute;top:658px;width:340px;text-align:center}
.feature .badge{width:116px;height:116px;border-radius:50%;background:#fff;margin:0 auto;box-shadow:0 3px 12px rgba(0,0,0,.18);display:flex;align-items:center;justify-content:center}
.feature .disc{width:78px;height:78px;border-radius:50%;background:var(--navy);display:flex;align-items:center;justify-content:center}
.feature h3{margin-top:26px;color:var(--navy);font-size:23px;font-weight:600;line-height:40px;text-transform:uppercase}

/* OFFERINGS */
.offer{position:absolute;top:906px;width:600px;height:359px;overflow:hidden}
.offer-quality .media{position:absolute;inset:0;background:linear-gradient(120deg,#8fa6c7 0%,#6f87ad 50%,#4e6590 100%)}
.offer-mdm .media{position:absolute;inset:0;background:linear-gradient(120deg,#e6be3c 0%,#d7ad34 55%,#b99128 100%)}
.offer h2{position:absolute;color:#fff;font-size:32px;font-weight:600;text-transform:uppercase;white-space:nowrap}
.offer ul{position:absolute;list-style:none;color:#fff;font-size:16px}
.offer li{display:flex;align-items:center;gap:8px;height:31px}
.offer-mdm li{justify-content:flex-end;flex-direction:row}
.tick{width:16px;height:16px;border-radius:50%;background:#fff;display:inline-flex;align-items:center;justify-content:center;flex:none}
.btn-yellow{position:absolute;background:var(--yellow);color:#fff;font-weight:600;display:flex;align-items:center;justify-content:center;text-transform:uppercase}
.offer .btn-yellow,.offer .btn-navy{width:207px;height:45px;font-size:13px;top:247px}

/* CONNECTORS */
.section-title{position:absolute;left:0;width:1200px;text-align:center;color:var(--navy);font-size:36px;font-weight:600;text-transform:uppercase}
.card{position:absolute;width:394px;height:262px;overflow:hidden;color:#fff;text-align:center}
.card.navy{background:var(--navy)}
.card.yellow{background:var(--yellow)}
.card.photo-a{background:linear-gradient(135deg,#3a4a6a,#2b3656 60%,#3a4c75)}
.card.photo-f{background:linear-gradient(135deg,#4e5460,#343943 60%,#22262e)}
.card.photo-s{background:linear-gradient(135deg,#6d6a63,#59544c 50%,#7a6a52)}
.card .frame{position:absolute;left:29px;top:20px;right:29px;bottom:20px;border:1.5px dashed rgba(255,255,255,.85)}
.card h3{position:absolute;top:52px;left:0;width:100%;font-size:22px;font-weight:600;text-transform:uppercase}
.card p{position:absolute;top:90px;left:40px;right:40px;font-size:15px;font-weight:500;line-height:31px}
.card .more{position:absolute;top:188px;left:0;width:100%;font-size:15px;font-weight:500;display:flex;justify-content:center;align-items:center;gap:6px}

/* SUPPORT */
.support{position:absolute;top:2012px;left:0;width:1200px;height:323px;background:var(--navy);color:#fff;text-align:center}
.support h2{position:absolute;top:36px;left:0;width:100%;font-size:36px;font-weight:600;text-transform:uppercase}
.support p{position:absolute;top:100px;left:130px;width:940px;font-size:17px;line-height:31px}
.pill{position:absolute;top:218px;height:55px;border-radius:28px;background:var(--yellow);color:#fff;font-size:19px;display:flex;align-items:center;justify-content:center;gap:10px}

/* FOOTER */
.footer{position:absolute;top:2335px;left:0;width:1200px;height:384px;background:var(--footer-bg)}
.footer h4{position:absolute;font-size:21px;font-weight:600;color:var(--ink);text-transform:uppercase;white-space:nowrap}
.f-logo{position:absolute;left:100px;top:80px;display:flex;align-items:center;gap:10px}
.f-logo .mark{width:30px;height:30px;border-radius:50%;background:var(--navy)}
.f-logo .name{font-size:30px;font-weight:600;color:var(--navy);line-height:1}
.f-text{position:absolute;font-size:13px;color:var(--ink);line-height:25px}
.soc{position:absolute;top:215px;width:30px;height:30px;border-radius:50%;border:1.5px solid var(--navy)}
.contact-row{position:absolute;left:341px;display:flex;gap:16px;font-size:14px;line-height:24px;color:var(--ink)}
.contact-row svg{flex:none;margin-top:4px}
.email-input{position:absolute;left:611px;top:188px;width:310px;height:45px;border:1px solid #d6d8dc;background:#fff;font-size:13px;color:#444;padding:0 14px;display:flex;align-items:center}
.links{position:absolute;left:961px;top:122px;list-style:none;font-size:14px;color:var(--ink)}
.links li{height:25px;display:flex;align-items:center;gap:14px}
.links li::before{content:"";border-left:5px solid var(--ink);border-top:4px solid transparent;border-bottom:4px solid transparent}
.copy{position:absolute;top:340px;left:0;width:1200px;text-align:center;font-size:14px;color:var(--ink)}
</style>
</head>
<body>

<header class="hero">
  <div class="hero-media" role="img" aria-label="Businessman in a suit facing a city skyline overlaid with glowing data dashboards and network graphics"></div>

  <div class="topbar">
    <div class="item" style="left:90px">
      <svg width="13" height="13" viewBox="0 0 24 24"><path fill="#fff" d="M6.6 10.8a15.1 15.1 0 0 0 6.6 6.6l2.2-2.2c.3-.3.7-.4 1-.2 1.1.4 2.3.6 3.6.6.6 0 1 .4 1 1V20c0 .6-.4 1-1 1A17 17 0 0 1 3 4c0-.6.4-1 1-1h3.5c.6 0 1 .4 1 1 0 1.3.2 2.5.6 3.6.1.3 0 .7-.2 1z"/></svg>
      (555) 014-2287
    </div>
    <div class="item" style="left:250px">
      <svg width="15" height="12" viewBox="0 0 20 15"><rect width="20" height="15" rx="1.5" fill="#fff"/><path d="M1 1l9 7 9-7" stroke="#3a5a88" stroke-width="1.6" fill="none"/></svg>
      info@zolvinbyte.example
    </div>
    <div class="item" style="left:842px">
      <svg width="13" height="14" viewBox="0 0 20 22"><circle cx="10" cy="6" r="5" fill="#fff"/><path d="M0 22c0-6 4.5-9 10-9s10 3 10 9z" fill="#fff"/></svg>
      login
    </div>
    <div class="item" style="left:922px">
      <svg width="15" height="14" viewBox="0 0 22 20"><path d="M2 10h10M8 5l5 5-5 5" stroke="#fff" stroke-width="2.4" fill="none"/><path d="M14 1h6v18h-6" stroke="#fff" stroke-width="2.4" fill="none"/></svg>
      Register
    </div>
    <div class="item" style="left:1018px">
      <svg width="18" height="12" viewBox="0 0 18 12"><rect width="18" height="12" fill="#2a3f88"/><path d="M0 0l18 12M18 0L0 12" stroke="#fff" stroke-width="2"/><path d="M9 0v12M0 6h18" stroke="#fff" stroke-width="3.4"/><path d="M9 0v12M0 6h18" stroke="#d22" stroke-width="1.8"/></svg>
      English
      <svg width="10" height="7" viewBox="0 0 10 7"><path d="M1 1l4 4 4-4" stroke="#fff" stroke-width="2" fill="none"/></svg>
    </div>
  </div>

  <div class="nav-logo"><span class="mark"></span><span class="name">Zolvinbyte</span></div>
  <div class="abs" style="left:200px;top:106px;color:#fff;font-size:12px;white-space:nowrap">Enterprise Data Quality Made Easy</div>

  <nav class="nav">
    <a style="left:0">Home</a>
    <a style="left:82px">About us</a>
    <a style="left:187px">Our Services</a>
    <a style="left:322px">Rich Connectors</a>
    <a style="left:490px">Support</a>
    <a style="left:588px">Contact</a>
  </nav>

  <div class="follow">
    <div class="dot"></div><div class="dot"></div><div class="dot"></div><div class="dot"></div><div class="dot"></div>
    <div class="line"></div>
    <div class="label">Follow us</div>
  </div>

  <h1 class="hero-title">ZOLVINBYTE</h1>
  <p class="hero-sub">Enterprise Data Quality and Master Data<br>Management Made Easy</p>
  <div class="btn-navy hero-btn">Read More</div>

  <div class="slider-dots"><span></span><span class="active"></span><span></span></div>
</header>

<section class="features">
  <div class="feature" style="left:89px">
    <div class="badge"><div class="disc">
      <svg width="40" height="40" viewBox="0 0 40 40" fill="none" stroke="#fff" stroke-width="2"><rect x="6" y="4" width="28" height="8" rx="1"/><rect x="6" y="14" width="28" height="8" rx="1"/><rect x="6" y="24" width="28" height="8" rx="1"/><circle cx="11" cy="8" r="1" fill="#fff"/><circle cx="11" cy="18" r="1" fill="#fff"/><circle cx="11" cy="28" r="1" fill="#fff"/><path d="M20 32v4M8 37h24"/></svg>
    </div></div>
    <h3>Cleanse Addresses<br>in 5 Minutes</h3>
  </div>
  <div class="feature" style="left:428px">
    <div class="badge"><div class="disc">
      <svg width="44" height="44" viewBox="0 0 44 44" fill="none" stroke="#fff" stroke-width="2"><circle cx="22" cy="22" r="17"/><path d="M8 15h28M6 22h32M8 29h28M22 5c-6 5-6 29 0 34M22 5c6 5 6 29 0 34"/></svg>
    </div></div>
    <h3>Match &amp; Merge<br>Records in 10 Minutes</h3>
  </div>
  <div class="feature" style="left:769px">
    <div class="badge"><div class="disc">
      <svg width="42" height="42" viewBox="0 0 42 42" fill="none" stroke="#fff" stroke-width="2"><rect x="8" y="4" width="26" height="18" rx="1"/><path d="M13 10h16M13 15h10"/><circle cx="21" cy="28" r="3"/><path d="M15 38c0-4 3-6 6-6s6 2 6 6M6 38h30"/></svg>
    </div></div>
    <h3>Master Records<br>in 60 Minutes</h3>
  </div>
</section>

<section class="offer offer-quality" style="left:0">
  <div class="media" role="img" aria-label="Analyst working at a computer in a bright office"></div>
  <h2 style="left:123px;top:84px">Data Quality</h2>
  <ul style="left:123px;top:134px">
    <li><span class="tick"><svg width="10" height="8" viewBox="0 0 10 8"><path d="M1 4l3 3 5-6" stroke="#6f87ad" stroke-width="2" fill="none"/></svg></span>Global Address Verification</li>
    <li><span class="tick"><svg width="10" height="8" viewBox="0 0 10 8"><path d="M1 4l3 3 5-6" stroke="#6f87ad" stroke-width="2" fill="none"/></svg></span>Data Cleansing/Enrichment</li>
    <li><span class="tick"><svg width="10" height="8" viewBox="0 0 10 8"><path d="M1 4l3 3 5-6" stroke="#6f87ad" stroke-width="2" fill="none"/></svg></span>Match and Merge</li>
  </ul>
  <div class="btn-yellow" style="left:123px;top:247px;width:207px;height:45px;font-size:13px">View More</div>
</section>

<section class="offer offer-mdm" style="left:600px">
  <div class="media" role="img" aria-label="Engineers reviewing a laptop in a server room"></div>
  <h2 style="left:52px;top:84px">Master Data Management</h2>
  <ul style="right:90px;top:134px">
    <li><span class="tick"><svg width="10" height="8" viewBox="0 0 10 8"><path d="M1 4l3 3 5-6" stroke="#d7ad34" stroke-width="2" fill="none"/></svg></span>Integration</li>
    <li><span class="tick"><svg width="10" height="8" viewBox="0 0 10 8"><path d="M1 4l3 3 5-6" stroke="#d7ad34" stroke-width="2" fill="none"/></svg></span>Mastering</li>
    <li><span class="tick"><svg width="10" height="8" viewBox="0 0 10 8"><path d="M1 4l3 3 5-6" stroke="#d7ad34" stroke-width="2" fill="none"/></svg></span>Governance</li>
  </ul>
  <div class="btn-navy" style="left:285px;top:247px;width:207px;height:45px;font-size:13px">View More</div>
</section>

<h2 class="section-title" style="top:1318px">Rich Connectors</h2>

<section class="connectors">
  <article class="card photo-a" style="left:0;top:1410px" role="img" aria-label="Developer working at a desk with monitors">
    <div class="frame"></div><h3>Applications</h3>
    <p>Sed ut perspiciatis unde omnis iste natus error sit voluptatem accusantium doloremque laudantium</p>
    <div class="more">Read More <svg width="13" height="13" viewBox="0 0 14 14"><circle cx="7" cy="7" r="7" fill="#fff"/><path d="M5.5 4l3 3-3 3" stroke="#2b3656" stroke-width="1.8" fill="none"/></svg></div>
  </article>
  <article class="card yellow" style="left:403px;top:1410px">
    <div class="frame"></div><h3>Databases</h3>
    <p>Sed ut perspiciatis unde omnis iste natus error sit voluptatem accusantium doloremque laudantium</p>
    <div class="more">Read More <svg width="13" height="13" viewBox="0 0 14 14"><circle cx="7" cy="7" r="7" fill="#fff"/><path d="M5.5 4l3 3-3 3" stroke="#fcc736" stroke-width="1.8" fill="none"/></svg></div>
  </article>
  <article class="card photo-f" style="left:806px;top:1410px" role="img" aria-label="Hands typing on a laptop keyboard">
    <div class="frame"></div><h3>Files</h3>
    <p>Sed ut perspiciatis unde omnis iste natus error sit voluptatem accusantium doloremque laudantium</p>
    <div class="more">Read More <svg width="13" height="13" viewBox="0 0 14 14"><circle cx="7" cy="7" r="7" fill="#fff"/><path d="M5.5 4l3 3-3 3" stroke="#343943" stroke-width="1.8" fill="none"/></svg></div>
  </article>
  <article class="card navy" style="left:0;top:1681px">
    <div class="frame"></div><h3>Batch</h3>
    <p>Sed ut perspiciatis unde omnis iste natus error sit voluptatem accusantium doloremque laudantium</p>
    <div class="more">Read More <svg width="13" height="13" viewBox="0 0 14 14"><circle cx="7" cy="7" r="7" fill="#fff"/><path d="M5.5 4l3 3-3 3" stroke="#1f2a6b" stroke-width="1.8" fill="none"/></svg></div>
  </article>
  <article class="card photo-s" style="left:403px;top:1681px" role="img" aria-label="Desk with papers and a laptop seen from above">
    <div class="frame"></div><h3>Streaming</h3>
    <p>Sed ut perspiciatis unde omnis iste natus error sit voluptatem accusantium doloremque laudantium</p>
    <div class="more">Read More <svg width="13" height="13" viewBox="0 0 14 14"><circle cx="7" cy="7" r="7" fill="#fff"/><path d="M5.5 4l3 3-3 3" stroke="#59544c" stroke-width="1.8" fill="none"/></svg></div>
  </article>
  <article class="card navy" style="left:806px;top:1681px">
    <div class="frame"></div><h3>Real Time/Interactive</h3>
    <p>Sed ut perspiciatis unde omnis iste natus error sit voluptatem accusantium doloremque laudantium</p>
    <div class="more">Read More <svg width="13" height="13" viewBox="0 0 14 14"><circle cx="7" cy="7" r="7" fill="#fff"/><path d="M5.5 4l3 3-3 3" stroke="#1f2a6b" stroke-width="1.8" fill="none"/></svg></div>
  </article>
</section>

<section class="support">
  <h2>Support</h2>
  <p>Sed ut perspiciatis unde omnis iste natus error sit voluptatem accusantium doloremque laudantium, totam rem aperiam, eaque ipsa quae ab illo inventore veritatis et quasi architecto beatae vitae dicta sunt explicabo. Nemo enim ipsam voluptatem quia voluptas sit aspernatur aut odit aut fugit.</p>
  <div class="pill" style="left:391px;width:215px">
    <svg width="16" height="16" viewBox="0 0 24 24"><path fill="#fff" d="M6.6 10.8a15.1 15.1 0 0 0 6.6 6.6l2.2-2.2c.3-.3.7-.4 1-.2 1.1.4 2.3.6 3.6.6.6 0 1 .4 1 1V20c0 .6-.4 1-1 1A17 17 0 0 1 3 4c0-.6.4-1 1-1h3.5c.6 0 1 .4 1 1 0 1.3.2 2.5.6 3.6.1.3 0 .7-.2 1z"/></svg>
    Click to call
  </div>
  <div class="pill" style="left:620px;width:188px">
    <svg width="18" height="18" viewBox="0 0 24 24"><path fill="#fff" d="M22 2L2 10l8 3 3 8z"/></svg>
    Contact us
  </div>
</section>

<footer class="footer">
  <div class="f-logo"><span class="mark"></span><span class="name">Zolvinbyte</span></div>
  <div class="abs" style="left:140px;top:114px;font-size:10px;color:var(--ink)">Enterprise Data Quality Made Easy</div>
  <p class="f-text" style="left:100px;top:132px;width:220px">Sed ut perspiciatis unde omnis iste natus error sit voluptatem accusantium dantium,</p>
  <span class="soc" style="left:100px"></span>
  <span class="soc" style="left:142px"></span>
  <span class="soc" style="left:183px"></span>

  <h4 style="left:341px;top:74px">Contact Us</h4>
  <div class="contact-row" style="top:134px">
    <svg width="14" height="18" viewBox="0 0 14 18"><path d="M7 0a7 7 0 0 1 7 7c0 5-7 11-7 11S0 12 0 7a7 7 0 0 1 7-7z" fill="#fcc736"/><circle cx="7" cy="7" r="2.6" fill="#fff"/></svg>
    <span>418 Larkspur Avenue, Suite 120<br>Hollowmere, CA 90001</span>
  </div>
  <div class="contact-row" style="top:196px">
    <svg width="14" height="14" viewBox="0 0 24 24"><path fill="#fcc736" d="M6.6 10.8a15.1 15.1 0 0 0 6.6 6.6l2.2-2.2c.3-.3.7-.4 1-.2 1.1.4 2.3.6 3.6.6.6 0 1 .4 1 1V20c0 .6-.4 1-1 1A17 17 0 0 1 3 4c0-.6.4-1 1-1h3.5c.6 0 1 .4 1 1 0 1.3.2 2.5.6 3.6.1.3 0 .7-.2 1z"/></svg>
    <span>Phone: (555) 014-2287</span>
  </div>
  <div class="contact-row" style="top:226px">
    <svg width="14" height="11" viewBox="0 0 20 15"><rect width="20" height="15" rx="1.5" fill="#fcc736"/><path d="M1 1l9 7 9-7" stroke="#fff" stroke-width="1.6" fill="none"/></svg>
    <span>Email: info@zolvinbyte.example</span>
  </div>

  <h4 style="left:611px;top:74px">Sign up for Newsletter</h4>
  <p class="f-text" style="left:611px;top:128px;width:320px;font-size:13px;line-height:22px">Want to make an impact? Provide your email and we'll be in touch.</p>
  <div class="email-input">Enter email</div>
  <div class="btn-yellow" style="left:611px;top:250px;width:127px;height:38px;font-size:15px">Sign Up</div>

  <h4 style="left:961px;top:74px">Quick Links</h4>
  <ul class="links">
    <li>Home</li><li>About us</li><li>Our Services</li><li>Rich Connectors</li><li>Support</li><li>Contact</li>
  </ul>

  <p class="copy">Copyrights © 2018 All Rights Reserved</p>
</footer>

</body>
</html>
```